Serial Entrepreneur Business Card: 4 Logo Design

I am a serial entrepreneur and a full time mechanical engineer. I have four businesses. I would like to display them all on one business card.
*Please see the attached PDF for the design requirements*

www.KelbroNest.com

Businesses
-KelbroNest
-Quiet Lantern Properties
-Torlen Products
-Drosk Harbor Cast

Target Market(s)

Clients, Entrepreneurs, Associates, really anyone. Should be very professional.

Industry/Entity Type

Entrepreneur

Contact Information for Business Card

3.5" x 2" Standard Business Card Size
** Please review the attached requirement PDF for in depth detail on what I am expecting**

Font styles to use
Sans Serif

Requirements
Must have
• My personal contact information:
• First Name: Dae hwan
• Last Name: Pellow
• Nick Name: Riko
• Address: 83 Tolmer Court, Brenvale OR 97391
• Phone Number: 503-574-2916
• Email: RikodPellow@mailnest.example
• Website: www.KelbroNest.com
• All Four Logos of the Companies I own:
• -KelbroNest
• -Quiet Lantern Properties
• -Torlen Products
• -Drosk Harbor Cast
• My Professions:
• -Prototyping Engineer
• -Real Estate Investor
• -Financial Blogger
• -Video Podcaster
• -Online Retail Seller
Nice to have
• If it fits, please include the website for each logo, if there is more space please include the email for each.
• It might be nice to have the QX GUILD Logo, or TOVRA logo for my full-time job. But only if it fits.

```html
<!DOCTYPE html>
<html lang="en">
<head>
<meta charset="utf-8">
<title>KelbroNest Business Card</title>
<link href="https://fonts.googleapis.com/css2?family=Poppins:wght@600;700;800&family=Open+Sans:wght@400;600&display=swap" rel="stylesheet">
<style>
  :root {
    --bg: #2b2b2b;
    --ink: #1f1f1f;
    --dark: #262626;
    --green: #11873f;
    --green-deep: #0c6e32;
    --light: #efefef;
    --white: #ffffff;
    --muted: #3a3a3a;
    --rule: #cfcfcf;
  }
  * { box-sizing: border-box; margin: 0; padding: 0; }
  html, body { width: 1200px; height: 900px; overflow: hidden; background: var(--bg); }
  .stage { position: relative; width: 1200px; height: 900px; }

  .card {
    position: absolute; left: 250px; width: 700px; height: 400px;
    border-radius: 22px; overflow: hidden; background: var(--white);
  }
  .card--front { top: 30px; display: flex; flex-direction: column; }
  .card--back { top: 470px; display: flex; }

  /* Front */
  .front__head {
    height: 165px; flex: none; background: var(--dark);
    border-bottom: 5px solid var(--green);
    display: flex; align-items: center; padding-left: 60px; gap: 16px;
  }
  .brand-mark { width: 26px; height: 26px; background: var(--green); }
  .brand-name {
    font-family: "Poppins", sans-serif; font-weight: 800; font-size: 78px;
    color: var(--white); letter-spacing: -1px; line-height: 1;
  }
  .front__body { position: relative; flex: 1; }
  .front__foot { height: 12px; flex: none; background: var(--green); }

  .person {
    position: absolute; left: 40px; top: 40px;
    font-family: "Poppins", sans-serif; font-weight: 700; font-size: 25px; color: var(--ink);
  }
  .person .nick { color: var(--green); }
  .venture-row {
    position: absolute; left: 40px; top: 100px; display: flex; gap: 16px; align-items: flex-end;
  }
  .venture-row .mark { width: 50px; height: 50px; }

  .contact {
    position: absolute; left: 400px; top: 36px; list-style: none;
    font-family: "Open Sans", sans-serif; font-size: 14px; color: var(--muted);
  }
  .contact li { display: flex; align-items: center; gap: 10px; height: 26px; }
  .contact svg { width: 16px; height: 16px; flex: none; }

  /* Back */
  .back__side {
    width: 170px; background: var(--dark); color: var(--white);
    display: flex; justify-content: center; align-items: center; gap: 8px;
  }
  .back__side .vline {
    writing-mode: vertical-rl; transform: rotate(180deg); white-space: nowrap;
  }
  .back__name { font-family: "Poppins", sans-serif; font-weight: 700; font-size: 26px; }
  .back__meta { font-family: "Open Sans", sans-serif; font-size: 13px; line-height: 1.35; }
  .back__rows { flex: 1; display: flex; flex-direction: column; }
  .role { flex: 1; display: flex; align-items: center; }
  .role--light { background: var(--light); }
  .role--green { background: var(--green); }
  .role__icon {
    width: 120px; height: 100%; display: flex; align-items: center; justify-content: center;
    border-right: 2px solid var(--rule);
  }
  .role--green .role__icon { border-right-color: var(--green-deep); }
  .role__icon .mark { width: 48px; height: 48px; }
  .role__text { padding-left: 26px; font-family: "Open Sans", sans-serif; }
  .role__title { font-family: "Poppins", sans-serif; font-weight: 600; font-size: 18px; line-height: 1.2; }
  .role__mail { font-size: 13px; }
  .role--light .role__title { color: var(--green); }
  .role--light .role__mail { color: var(--muted); }
  .role--green .role__title { color: var(--white); }
  .role--green .role__mail { color: var(--white); }
  .role--plain .role__title { color: var(--ink); }
</style>
</head>
<body>
<main class="stage">

  <section class="card card--front">
    <header class="front__head">
      <span class="brand-mark"></span>
      <span class="brand-name">KelbroNest</span>
    </header>
    <div class="front__body">
      <h1 class="person">Dae hwan <span class="nick">"Riko"</span> Pellow</h1>
      <div class="venture-row">
        <svg class="mark" role="img" aria-label="QX GUILD badge"><rect width="50" height="50" rx="4" fill="#1f1f1f"/></svg>
        <svg class="mark" role="img" aria-label="KelbroNest mark: family on tandem bicycle"><rect width="50" height="50" rx="4" fill="#2f2f2f"/></svg>
        <svg class="mark" role="img" aria-label="Torlen Products mark: bird"><rect width="50" height="50" rx="4" fill="#1f1f1f"/></svg>
        <svg class="mark" role="img" aria-label="Quiet Lantern Properties mark: house"><rect width="50" height="50" rx="4" fill="#1f1f1f"/></svg>
        <svg class="mark" role="img" aria-label="Drosk Harbor Cast mark"><rect width="50" height="50" rx="4" fill="#11873f"/></svg>
      </div>
      <ul class="contact">
        <li><svg viewBox="0 0 16 16"><rect x="4" y="1" width="8" height="14" rx="1.5" fill="none" stroke="#555"/><circle cx="8" cy="12.5" r=".8" fill="#555"/></svg>+503 574 2916</li>
        <li><svg viewBox="0 0 16 16"><rect x="1" y="3.5" width="14" height="9" fill="none" stroke="#555"/><path d="M1 3.5 8 9l7-5.5" fill="none" stroke="#555"/></svg>RikodPellow@mailnest.example</li>
        <li><svg viewBox="0 0 16 16"><circle cx="8" cy="8" r="6.5" fill="none" stroke="#555"/><ellipse cx="8" cy="8" rx="3" ry="6.5" fill="none" stroke="#555"/><path d="M1.5 8h13" stroke="#555"/></svg>www.KelbroNest.com</li>
        <li><svg viewBox="0 0 16 16"><path d="M8 15s5-5.5 5-9A5 5 0 0 0 3 6c0 3.5 5 9 5 9z" fill="none" stroke="#555"/><circle cx="8" cy="6" r="1.8" fill="none" stroke="#555"/></svg>83 Tolmer Court, Brenvale OR 97391</li>
      </ul>
    </div>
    <div class="front__foot"></div>
  </section>

  <section class="card card--back">
    <aside class="back__side">
      <div class="vline back__name">Dae hwan "Riko" Pellow</div>
      <div class="vline back__meta">RikodPellow@mailnest.example<br>www.KelbroNest.com</div>
    </aside>
    <div class="back__rows">
      <div class="role role--light">
        <div class="role__icon"><svg class="mark" role="img" aria-label="QX GUILD badge"><rect width="48" height="48" rx="4" fill="#1f1f1f"/></svg></div>
        <div class="role__text"><div class="role__title">Prototyping Engineer</div><div class="role__mail">daehwan.r.pellow.civ@tovra.example</div></div>
      </div>
      <div class="role role--green">
        <div class="role__icon"><svg class="mark" role="img" aria-label="KelbroNest mark: family on tandem bicycle"><rect width="48" height="48" rx="4" fill="#1f1f1f"/></svg></div>
        <div class="role__text"><div class="role__title">Financial Blogger</div><div class="role__mail">rikopellow@mailnest.example</div></div>
      </div>
      <div class="role role--light">
        <div class="role__icon"><svg class="mark" role="img" aria-label="Torlen Products mark: bird"><rect width="48" height="48" rx="4" fill="#1f1f1f"/></svg></div>
        <div class="role__text"><div class="role__title">Online Retail Seller</div><div class="role__mail">sales@torlenproducts.example</div></div>
      </div>
      <div class="role role--green">
        <div class="role__icon"><svg class="mark" role="img" aria-label="Quiet Lantern Properties mark: house"><rect width="48" height="48" rx="4" fill="#1f1f1f"/></svg></div>
        <div class="role__text"><div class="role__title">Real Estate Investor</div><div class="role__mail">riko@quietlanternproperties.example</div></div>
      </div>
      <div class="role role--light role--plain">
        <div class="role__icon"><svg class="mark" role="img" aria-label="Drosk Harbor Cast mark"><rect width="48" height="48" rx="4" fill="#11873f"/></svg></div>
        <div class="role__text"><div class="role__title">Vlogger</div><div class="role__mail">media@droskharborcast.example</div></div>
      </div>
    </div>
  </section>

</main>
</body>
</html>
```